Laundromat Grand Opening.

Laundromat /Grand opening. One side English, one side Spanish. Include the Address, Name, Raffle/Prizes and Grand opening date.
Elmridge Wash Laundromat, 415 W. Harlan Ave. 2/7/2016. (555) 314-2297.

Coin

000000

• Eye catching. Laundry theme.

```html
<!DOCTYPE html>
<html lang="en">
<head>
<meta charset="utf-8">
<title>Elmridge Wash Laundromat – Grand Opening</title>
<link rel="stylesheet" href="https://fonts.googleapis.com/css2?family=Anton&family=Bebas+Neue&family=Lato:wght@400;700;900&family=Roboto+Condensed:wght@700&display=swap">
<style>
  :root {
    --page-bg: #e9e9e9;
    --ink: #0b0b0b;
    --brand-blue: #3b76c6;
    --white: #ffffff;
    --paper-light: #fbfbfb;
    --paper-shade: #dcdcdc;
    --steel-light: #d9dee4;
    --steel-mid: #8f9aa6;
    --steel-dark: #2f3944;
  }
  * { margin: 0; padding: 0; box-sizing: border-box; }
  html, body {
    width: 1200px; height: 888px; overflow: hidden;
    background: var(--page-bg);
  }
  .flyer {
    position: absolute; left: 60px; top: 78px;
    width: 1080px; height: 732px; overflow: hidden;
    background: linear-gradient(180deg, var(--paper-light) 0%, var(--paper-shade) 100%);
    box-shadow: 0 6px 18px rgba(0,0,0,0.25);
  }
  .flyer-shapes { position: absolute; inset: 0; }
  .headline {
    position: absolute; right: 30px; width: 420px; text-align: center;
    font-family: "Anton", sans-serif; font-weight: 400; line-height: 1;
    text-transform: uppercase; white-space: nowrap;
  }
  .headline-grand { top: 14px; font-size: 138px; color: var(--white); letter-spacing: 4px; }
  .headline-opening { top: 168px; font-size: 108px; color: var(--brand-blue); letter-spacing: 2px; }
  .event-date {
    position: absolute; left: 552px; top: 392px;
    font-family: "Bebas Neue", sans-serif; font-weight: 400;
    font-size: 88px; line-height: 1; color: var(--ink); letter-spacing: 1px;
    white-space: nowrap;
  }
  .event-time {
    position: absolute; left: 552px; top: 494px;
    font-family: "Bebas Neue", sans-serif; font-weight: 400;
    font-size: 41px; line-height: 1; color: var(--ink); white-space: nowrap;
  }
  .contact-box {
    position: absolute; left: 513px; top: 554px; width: 567px; height: 156px;
    background: var(--brand-blue); border-radius: 14px 0 0 14px;
    color: var(--white); font-family: "Lato", sans-serif; font-style: normal;
    padding: 8px 30px 0 0; text-align: right;
  }
  .contact-name { font-weight: 900; font-size: 29px; line-height: 42px; letter-spacing: 0.5px; text-transform: uppercase; white-space: nowrap; }
  .contact-line { font-weight: 400; font-size: 36px; line-height: 48px; display: flex; justify-content: flex-end; align-items: center; gap: 6px; white-space: nowrap; }
  .contact-line svg { width: 30px; height: 30px; fill: var(--white); }
  .raffle-badge {
    position: absolute; left: 145px; top: 397px; width: 300px; height: 300px;
  }
  .raffle-text {
    position: absolute; inset: 0; display: flex; flex-direction: column;
    justify-content: center; align-items: center;
    font-family: "Roboto Condensed", sans-serif; font-weight: 700;
    font-size: 72px; line-height: 1; color: var(--brand-blue);
  }
</style>
</head>
<body>
  <main class="flyer">
    <svg class="flyer-shapes" viewBox="0 0 1080 732" width="1080" height="732">
      <defs>
        <linearGradient id="washer-tones" x1="0" y1="0" x2="1" y2="1">
          <stop offset="0" stop-color="var(--steel-light)"/>
          <stop offset="0.45" stop-color="var(--steel-mid)"/>
          <stop offset="1" stop-color="var(--steel-dark)"/>
        </linearGradient>
      </defs>
      <path class="header-panel" d="M560,0 H1080 V402 C950,330 760,300 555,370 Z" fill="var(--ink)"/>
      <path class="header-rule" d="M555,370 C760,300 950,330 1080,402" fill="none" stroke="var(--brand-blue)" stroke-width="8"/>
      <path class="base-swoosh" d="M0,560 C110,578 210,582 300,574" fill="none" stroke="var(--brand-blue)" stroke-width="16"/>
      <path class="photo-frame" d="M0,0 H614 C700,170 630,420 440,520 C300,585 130,580 0,552 Z" fill="var(--brand-blue)"/>
      <path class="washer-photo" role="img" aria-label="Photo of front-loading laundromat washing machines"
            d="M0,0 H602 C684,170 616,410 432,506 C296,568 130,566 0,540 Z" fill="url(#washer-tones)"/>
    </svg>

    <h1>
      <span class="headline headline-grand">Grand</span>
      <span class="headline headline-opening">Opening</span>
    </h1>

    <p class="event-date">FEB 7TH. 2016</p>
    <p class="event-time">TIME 7:00 A.M TILL 10:00P.M.</p>

    <div class="raffle-badge">
      <svg viewBox="0 0 300 300" width="300" height="300">
        <polygon class="starburst" fill="var(--ink)" points="
          150,0 163,21 180,3 187,27 208,12 209,37 233,27 228,52 253,47 243,70 268,70 253,91 278,96 259,113 282,123 260,136 280,150 260,164 282,177 259,187 278,204 253,209 268,230 243,230 253,253 228,248 233,273 209,263 208,288 187,273 180,297 163,279 150,300 137,279 120,297 113,273 92,288 91,263 67,273 72,248 47,253 57,230 32,230 47,209 22,204 41,187 18,177 40,164 20,150 40,136 18,123 41,113 22,96 47,91 32,70 57,70 47,47 72,52 67,27 91,37 92,12 113,27 120,3 137,21"/>
      </svg>
      <div class="raffle-text"><span>Raffle</span><span>Prizes</span></div>
    </div>

    <address class="contact-box">
      <div class="contact-name">Elmridge Wash Laundromat</div>
      <div class="contact-line">
        <svg viewBox="0 0 24 24" aria-hidden="true"><path d="M6.6 10.8a15.1 15.1 0 0 0 6.6 6.6l2.2-2.2a1 1 0 0 1 1-.25 11.4 11.4 0 0 0 3.6.6 1 1 0 0 1 1 1V20a1 1 0 0 1-1 1A17 17 0 0 1 3 4a1 1 0 0 1 1-1h3.5a1 1 0 0 1 1 1c0 1.25.2 2.45.6 3.6a1 1 0 0 1-.25 1z"/></svg>
        <span>(555)314-2297</span>
      </div>
      <div class="contact-line">
        <svg viewBox="0 0 24 24" aria-hidden="true"><path d="M12 2a7 7 0 0 0-7 7c0 5.25 7 13 7 13s7-7.75 7-13a7 7 0 0 0-7-7zm0 9.5A2.5 2.5 0 1 1 12 6.5a2.5 2.5 0 0 1 0 5z"/></svg>
        <span>415 W. Harlan Ave. 48213</span>
      </div>
    </address>
  </main>
</body>
</html>
```